Business Card - connecting 2 souls and beggining the journey of self discovery

Logo on the front
with tag line

On the back list of services and contact details

Seminars
workshops
Coaching
podcasts

Darren Whitlow
Health & Wellbeing Life Coach
0468 215 937
darren@wearebrightroots.net
wearebrightroots.net

Industry/Entity Type

Life Coaching

Contact Information for Business Card

I like the use of colour from the logo to be used. I'm not a fan of white.

Requirements
Must have
• My tagline: the path to wellness begins within
Nice to have
• Use of colour that is in the mind body soul logo

```html
<!DOCTYPE html>
<html lang="en">
<head>
<meta charset="utf-8">
<title>Bright Roots Wellness – Business Card</title>
<link rel="stylesheet" href="https://fonts.googleapis.com/css2?family=Open+Sans:ital,wght@0,400;0,700;1,400&display=swap">
<style>
  :root {
    --backdrop: #2f1c14;
    --card: #ffffff;
    --ink: #4d4d4d;
    --rule: #555555;
    --purple: #8f4fa3;
    --orange: #f3922a;
    --green: #6dbd72;
    --charcoal: #4a4a4a;
    --brand-grey: #7a7a7a;
  }
  * { box-sizing: border-box; margin: 0; padding: 0; }
  html, body {
    width: 1200px;
    height: 1000px;
    overflow: hidden;
    background: var(--backdrop);
    font-family: "Open Sans", Arial, sans-serif;
    color: var(--ink);
  }
  .canvas { position: relative; width: 1200px; height: 1000px; }

  .card {
    position: absolute;
    width: 425px;
    height: 243px;
    background: var(--card);
    box-shadow: 0 3px 10px rgba(0,0,0,0.45);
    overflow: hidden;
  }

  /* Contact side */
  .card--contact { left: 262px; top: 286px; text-align: center; }
  .contact__name { margin-top: 58px; font-size: 17px; font-weight: 700; line-height: 1.2; }
  .contact__role { font-size: 14px; line-height: 1.3; }
  .services {
    list-style: none;
    width: 265px;
    margin: 9px auto 0;
    padding: 6px 0 7px;
    border-top: 1px solid var(--rule);
    border-bottom: 1px solid var(--rule);
    font-size: 13.5px;
    display: flex;
    justify-content: center;
    gap: 6px;
    white-space: nowrap;
  }
  .services__item::before {
    content: "";
    display: inline-block;
    width: 6px; height: 6px;
    border-radius: 50%;
    margin-right: 4px;
    vertical-align: middle;
    background: var(--dot);
  }
  .services__item--seminars { --dot: var(--orange); }
  .services__item--workshops { --dot: var(--purple); }
  .services__item--coaching { --dot: var(--green); }
  .services__item--podcasts { --dot: var(--charcoal); }
  .contact__details { margin-top: 10px; font-size: 13.5px; line-height: 1.25; }
  .colour-band {
    position: absolute; left: 0; right: 0; bottom: 0;
    height: 14px; display: flex;
  }
  .colour-band span { display: block; height: 100%; }
  .colour-band__purple { flex: 0 0 82%; background: var(--purple); }
  .colour-band__orange { flex: 0 0 9%; background: var(--orange); }
  .colour-band__green { flex: 0 0 6%; background: var(--green); }
  .colour-band__charcoal { flex: 1; background: var(--charcoal); }

  /* Brand side */
  .card--brand { left: 481px; top: 545px; text-align: center; }
  .brand__mark {
    width: 78px; height: 78px; border-radius: 50%;
    margin: 60px auto 0;
    background: var(--orange);
  }
  .brand__name {
    margin-top: 18px;
    font-size: 19px;
    font-weight: 400;
    color: var(--brand-grey);
    letter-spacing: -0.3px;
    line-height: 1.2;
  }
  .brand__tagline {
    font-size: 12px;
    font-style: italic;
    color: var(--brand-grey);
    line-height: 1.2;
  }
</style>
</head>
<body>
<main class="canvas">
  <section class="card card--contact">
    <h1 class="contact__name">Darren Whitlow</h1>
    <p class="contact__role">Life Coach</p>
    <ul class="services">
      <li class="services__item services__item--seminars">Seminars</li>
      <li class="services__item services__item--workshops">Workshops</li>
      <li class="services__item services__item--coaching">Coaching</li>
      <li class="services__item services__item--podcasts">Podcasts</li>
    </ul>
    <p class="contact__details">
      0468 215 937<br>
      darren@wearebrightroots.net<br>
      wearebrightroots.net
    </p>
    <div class="colour-band">
      <span class="colour-band__purple"></span>
      <span class="colour-band__orange"></span>
      <span class="colour-band__green"></span>
      <span class="colour-band__charcoal"></span>
    </div>
  </section>

  <section class="card card--brand">
    <div class="brand__mark"></div>
    <p class="brand__name">Bright Roots Wellness</p>
    <p class="brand__tagline">“ the path to wellness begins within ”</p>
  </section>
</main>
</body>
</html>
```